UPDATE: I have uploaded the selected logo from the other contest, please use it in your designs.

I have a logo design contest as well so not sure how PixelGuild handles that. They should integrate at some point. I will describe the overall theme with the logo description. See it for details.

The business card side of it would just build on that same theme.

Target Market(s)

8-40

Industry/Entity Type

Business

Contact Information for Business Card

FirstName LastName
Email

Logo Text

Velimor

Font styles to use
Sans Serif

Requirements
Must have
• the url Velimor.com somewhere in it.

```html
<!DOCTYPE html>
<html lang="en">
<head>
<meta charset="utf-8">
<title>Velimor — Business Card</title>
<link rel="stylesheet" href="https://fonts.googleapis.com/css2?family=Michroma&display=swap">
<style>
  :root {
    --page-bg: #f2f4f6;
    --card-deep: #2f78c0;
    --card-mid: #5aa6dc;
    --card-light: #cfeaf6;
    --band-blue: rgba(40, 110, 185, 0.82);
    --band-edge: #c8ccd2;
    --band-edge-dark: #7d8590;
    --brand-green: #86c83a;
    --brand-blue: #1c6fb8;
    --ink-navy: #16224a;
  }

  html, body {
    margin: 0;
    width: 1200px;
    height: 900px;
    overflow: hidden;
    background: var(--page-bg);
    font-family: "Michroma", sans-serif;
  }

  .card {
    position: absolute;
    left: 120px;
    top: 147px;
    width: 960px;
    height: 606px;
    border-radius: 44px;
    overflow: hidden;
    box-shadow: 0 18px 40px rgba(0, 0, 0, 0.18);
  }

  .card__backdrop {
    position: absolute;
    inset: 0;
    background:
      radial-gradient(ellipse at 85% 20%, var(--card-light) 0%, rgba(207, 234, 246, 0) 55%),
      linear-gradient(100deg, var(--card-deep) 0%, var(--card-mid) 45%, var(--card-light) 100%);
  }

  .brand {
    position: absolute;
    top: 138px;
    left: 0;
    right: 0;
    display: flex;
    justify-content: center;
    align-items: center;
    gap: 26px;
  }

  .brand__dot {
    width: 34px;
    height: 34px;
    border-radius: 50%;
    background: var(--brand-blue);
  }

  .brand__name {
    font-size: 84px;
    letter-spacing: 10px;
    color: var(--brand-blue);
    line-height: 1;
  }

  .band {
    position: absolute;
    left: 0;
    right: 0;
    top: 318px;
    height: 222px;
    background: var(--band-blue);
    border-top: 6px solid var(--band-edge);
    border-bottom: 6px solid var(--band-edge);
    box-shadow:
      inset 0 2px 0 var(--band-edge-dark),
      inset 0 -2px 0 var(--band-edge-dark);
    text-align: center;
  }

  .band__name {
    margin: 34px 0 0;
    font-size: 44px;
    font-weight: 400;
    letter-spacing: 2px;
    color: var(--brand-green);
    text-transform: uppercase;
  }

  .band__contact {
    margin: 40px 0 0;
    font-size: 27px;
    line-height: 1.3;
    letter-spacing: 1px;
    color: var(--ink-navy);
    text-transform: uppercase;
  }
</style>
</head>
<body>
  <article class="card">
    <div class="card__backdrop" role="img" aria-label="Blue gradient background with a fine white perspective grid pattern"></div>

    <header class="brand">
      <span class="brand__dot"></span>
      <span class="brand__name">VELIMOR</span>
    </header>

    <section class="band">
      <h1 class="band__name">Mara Quinlan</h1>
      <p class="band__contact">info@velimor.com<br>www.velimor.com</p>
    </section>
  </article>
</body>
</html>
```